New Web Design Project

New Roofing Website homepage mockup

Complete design document here: https://files.plorvex.net/doc/7tQmZrA2kLwP9xVbN4cYhE3sJdF8gUoR6iKe1nTy/edit?usp=sharing
Updates

Number of Pages Required

1 page

Font styles to use
Sans Serif

```html
<!DOCTYPE html>
<html lang="en">
<head>
<meta charset="utf-8">
<title>Keystone Roofing</title>
<link href="https://fonts.googleapis.com/css2?family=Open+Sans:wght@400;600;700;800&display=swap" rel="stylesheet">
<style>
:root{
  --blue:#1b8fd6;
  --blue-light:#4fb0df;
  --ink:#222;
  --text:#444;
  --muted:#8a8a8a;
  --ghost:#e4e4e6;
  --panel:#f0f0f2;
  --card:#e1e1e3;
  --black:#000;
  --white:#fff;
}
*{margin:0;padding:0;box-sizing:border-box}
html,body{width:1200px;height:4231px;overflow:hidden}
body{position:relative;font-family:'Open Sans',Arial,sans-serif;color:var(--text);background:var(--white)}
.abs{position:absolute}
/* header */
.brand{left:274px;top:18px;width:100px;text-align:center}
.brand-name{font-size:11px;font-weight:700;color:var(--blue);letter-spacing:.5px;line-height:1;white-space:nowrap}
.brand-mark{display:block;width:12px;height:12px;background:var(--blue);border-radius:50%;margin:0 auto 6px}
.nav{left:492px;top:28px;display:flex;gap:19px;font-size:8.5px;color:#555;text-transform:uppercase;letter-spacing:.3px}
.nav .active{color:var(--blue)}
/* hero */
.hero{left:0;top:63px;width:1200px;height:437px;background:linear-gradient(180deg,#3e5566 0%,#6d7b86 35%,#8a8f92 60%,#4f6a3a 88%,#3f5a2c 100%)}
.hero-title{left:0;top:218px;width:1210px;text-align:center;font-size:38px;font-weight:800;color:var(--white);letter-spacing:-1px}
.hero-title span{color:var(--blue)}
.btn{background:var(--blue);color:var(--white);font-weight:700;text-transform:uppercase;text-align:center;border-radius:2px}
.hero-btn{left:506px;top:304px;width:188px;height:29px;line-height:29px;font-size:9px}
/* features */
.feature-card{left:382px;top:500px;width:418px;height:242px;background:var(--white);box-shadow:0 10px 25px rgba(0,0,0,.08)}
.feature{width:280px;text-align:center}
.feature svg{display:block;margin:0 auto}
.feature h3{font-size:11.5px;font-weight:600;color:var(--ink);margin-top:10px}
.feature.active h3{color:var(--blue)}
.feature p{font-size:9px;line-height:16px;color:var(--muted);margin-top:9px}
/* section titles */
.section-title{left:0;width:1200px;text-align:center;font-size:62px;font-weight:800;color:var(--ghost);letter-spacing:1px}
/* services */
.service{width:240px}
.service h3{position:absolute;left:47px;top:-4px;font-size:12px;font-weight:700;color:var(--ink);white-space:nowrap}
.service p{position:absolute;left:47px;top:24px;width:170px;font-size:9px;line-height:17px;color:var(--muted)}
.icon-dot{position:absolute;left:0;top:0;width:30px;height:30px;border-radius:50%;background:var(--blue-light)}
.service svg{position:absolute;left:6px;top:-4px}
.frame-blue{left:903px;top:950px;width:62px;height:332px;background:var(--blue)}
.crew-photo{left:753px;top:969px;width:186px;height:297px;border:3px solid var(--white);background:linear-gradient(170deg,#8fcaf0 0%,#6aa7d8 45%,#3f78b8 75%,#c86d2f 100%)}
/* about */
.about-band{left:0;top:1348px;width:1200px;height:484px;background:var(--panel)}
.block-black{left:235px;top:1505px;width:69px;height:215px;background:var(--black)}
.block-blue{left:443px;top:1538px;width:118px;height:169px;background:var(--blue-light)}
.team-photo{left:243px;top:1528px;width:292px;height:155px;border:3px solid var(--white);background:linear-gradient(180deg,#cfd8d2 0%,#9aa39a 40%,#1d2224 60%,#3d4b3a 100%)}
.about-lead{left:609px;top:1492px;width:350px;font-size:11px;line-height:18.7px;color:#333}
.about-rule{left:609px;top:1653px;width:169px;height:1px;background:#999}
.about-body{left:609px;top:1668px;width:350px;font-size:9.3px;line-height:18.5px;color:var(--muted)}
.read-more{left:609px;top:1776px;font-size:11px;color:var(--blue);text-decoration:underline}
/* roof types */
.tabs{left:235px;top:2006px;width:730px;height:31px;background:var(--black);display:flex;font-size:10px;color:var(--white)}
.tabs div{text-align:center;line-height:31px}
.tabs .active{background:var(--blue-light)}
.tile{width:231px;height:127px}
/* projects */
.projects-band{left:0;top:2251px;width:1200px;height:622px;background:var(--panel)}
.project{width:232px;height:170px}
.project-label{display:flex;align-items:center;justify-content:center;font-size:19px;color:var(--white);background:linear-gradient(180deg,#2c2c2e,#1e1f21)}
.dots{left:577px;top:2837px;display:flex;gap:8px}
.dots i{display:block;width:6px;height:6px;border-radius:50%;background:#c8c8cc}
.dots i.on{background:#8fb8d8}
/* estimate */
.step{width:169px;border-bottom:1px solid #aaa;padding-bottom:3px;font-size:10px;color:#333;white-space:nowrap}
.step b{font-size:15px;font-weight:600;margin-right:8px}
.est-card{width:168px;height:311px;background:var(--card);text-align:center}
.est-swatch{height:142px}
.est-card .grade{margin-top:22px;font-size:10.5px;color:#666}
.est-card .model{margin-top:8px;font-size:10.5px;color:#666}
.est-card .price{margin-top:6px;font-size:13px;font-weight:700;color:#777}
.est-card .info{margin-top:6px;font-size:8px;color:#333}
.est-card .btn{width:141px;height:29px;line-height:27px;font-size:8px;margin:8px auto 0;border:1px solid #fff;border-radius:4px}
/* testimonial */
.quote{left:361px;top:3636px;width:478px;height:204px;background:#dcdcde;border-radius:3px;padding:22px 34px;font-size:10.3px;line-height:21.8px;color:var(--muted)}
.quote-tail{left:471px;top:3838px;width:0;height:0;border-left:9px solid transparent;border-right:9px solid transparent;border-top:10px solid #dcdcde}
.client{left:420px;top:3859px;width:120px;text-align:center}
.client b{display:block;font-size:14px;font-weight:600;color:#333}
.client span{font-size:9.5px;color:#555}
.chev{top:3708px;font-size:46px;color:#c9c9cc;font-weight:300}
/* footer */
.footer{left:0;top:4004px;width:1200px;height:227px;background:var(--black)}
.f-brand{left:225px;top:4070px;width:190px;text-align:center}
.f-brand .brand-mark{width:22px;height:22px;margin-bottom:10px}
.f-brand .brand-name{font-size:19px;color:var(--blue);letter-spacing:0}
.f-addr{left:235px;top:4158px;width:170px;text-align:center;font-size:8.5px;line-height:18px;color:#aaa}
.f-head{top:4049px;font-size:11px;font-weight:700;color:var(--blue)}
.f-links{font-size:7.5px;line-height:20px;color:#ccc;text-transform:uppercase}
.f-contact{left:796px;top:4089px;font-size:7.5px;color:#ccc}
.f-contact div{display:flex;align-items:center;gap:8px;height:25px}
.f-social{left:796px;top:4168px;display:flex;gap:13px}
.f-social i{display:block;width:11px;height:11px;border:1px solid var(--blue);border-radius:50%}
</style>
</head>
<body>

<header>
  <div class="abs brand"><span class="brand-mark"></span><div class="brand-name">KEYSTONE ROOFING</div></div>
  <nav class="abs nav"><span class="active">Home</span><span>Keystone Roofing</span><span>Blog</span><span>Reviews</span><span>About</span><span>Services</span><span>Affiliations</span><span>Contact</span></nav>
</header>

<section>
  <div class="abs hero" role="img" aria-label="Photo of a large grey two-storey house with a new shingle roof, trees and lawn"></div>
  <h1 class="abs hero-title">BUILT <span>RIGHT</span>, BUILT TO <span>LAST</span></h1>
  <div class="abs btn hero-btn">Get an instant estimate</div>
</section>

<section>
  <div class="abs feature-card"></div>
  <div class="abs feature" style="left:68px;top:570px">
    <svg width="38" height="38" viewBox="0 0 38 38" fill="none" stroke="#222" stroke-width="1.6"><path d="M4 30h30M6 25l26-10M6 20l22-8M10 24v6M30 17v13M24 8v6M22 8h4"/></svg>
    <h3>Roof Installation</h3><p>Aorem ipsum dolor sit amet, consectetur adipisc-<br>ing elit, sed do eiusmod tempor</p></div>
  <div class="abs feature active" style="left:451px;top:570px">
    <svg width="38" height="38" viewBox="0 0 38 38" fill="none" stroke="#1b8fd6" stroke-width="1.6"><path d="M4 18L19 5l15 13M8 15v17h22V15M15 32v-9h8v9M26 7v5"/></svg>
    <h3>Roof Repair</h3><p>Aorem ipsum dolor sit amet, consectetur adipiscing elit,<br>sed do eiusmod tempor</p></div>
  <div class="abs feature" style="left:861px;top:570px">
    <svg width="38" height="38" viewBox="0 0 38 38" fill="none" stroke="#222" stroke-width="1.6"><path d="M3 20L14 7h14l7 13M6 18v14h26V18M14 7l8 13M12 24h6v8M24 24h5v4h-5z"/></svg>
    <h3>Additional Services</h3><p>Aorem ipsum dolor sit amet, consectetur adipiscing elit,<br>sed do eiusmod tempor</p></div>
</section>

<section>
  <h2 class="abs section-title" style="top:812px">All Services</h2>
  <div class="abs service" style="left:228px;top:958px"><span class="icon-dot"></span><svg width="30" height="30" viewBox="0 0 30 30" fill="none" stroke="#222" stroke-width="1.4"><path d="M3 24h24M5 20l20-7M5 16l17-6M19 6v4"/></svg><h3>Roof Installation</h3><p>Aorem ipsum dolor sit amet, consect etur adipiscing elit, sed .</p></div>
  <div class="abs service" style="left:477px;top:955px"><span class="icon-dot"></span><svg width="30" height="30" viewBox="0 0 30 30" fill="none" stroke="#222" stroke-width="1.4"><path d="M3 14L15 4l12 10M6 12v14h18V12M12 26v-7h6v7"/></svg><h3>Roof Repair</h3><p>Aorem ipsum dolor sit amet, consect etur adipiscing elit, sed .</p></div>
  <div class="abs service" style="left:228px;top:1081px"><span class="icon-dot"></span><svg width="30" height="30" viewBox="0 0 30 30" fill="none" stroke="#222" stroke-width="1.4"><path d="M3 14L15 4l12 10M6 12v14h18V12M11 15h8v8h-8zM15 15v8M11 19h8"/></svg><h3>Windows/Skylights</h3><p>Aorem ipsum dolor sit amet, consect etur adipiscing elit, sed .</p></div>
  <div class="abs service" style="left:477px;top:1079px"><span class="icon-dot"></span><svg width="30" height="30" viewBox="0 0 30 30" fill="none" stroke="#222" stroke-width="1.4"><path d="M3 15L15 5l12 10M6 13v13h18V13M2 15h26M12 20h6v6h-6z"/></svg><h3>Gutters</h3><p>Aorem ipsum dolor sit amet, consect etur adipiscing elit, sed .</p></div>
  <div class="abs service" style="left:228px;top:1200px"><span class="icon-dot"></span><svg width="30" height="30" viewBox="0 0 30 30" fill="none" stroke="#222" stroke-width="1.4"><path d="M4 8h22v18H4zM4 13h22M4 19h22M11 8v18M19 8v18"/></svg><h3>Siding</h3><p>Aorem ipsum dolor sit amet, consect etur adipiscing elit, sed .</p></div>
  <div class="abs service" style="left:477px;top:1200px"><span class="icon-dot"></span><svg width="30" height="30" viewBox="0 0 30 30" fill="none" stroke="#222" stroke-width="1.4"><path d="M8 6v10a7 7 0 0014 0V6M12 6v9M18 6v9M15 22v5"/></svg><h3>Interior leak damage repairs</h3><p>Aorem ipsum dolor sit amet, consect etur adipiscing elit, sed .</p></div>
  <div class="abs frame-blue"></div>
  <div class="abs crew-photo" role="img" aria-label="Photo of roofing crew in hard hats and blue work shirts"></div>
</section>

<section>
  <div class="abs about-band"></div>
  <h2 class="abs section-title" style="top:1363px">About</h2>
  <div class="abs block-black"></div>
  <div class="abs block-blue"></div>
  <div class="abs team-photo" role="img" aria-label="Photo of the roofing team standing beside a black company pickup truck"></div>
  <p class="abs about-lead">After over a decade of general contracting we continue to see a re-petitive trend by the roof purchase process where home owners are constantly left confused, nervous and worried when they need a new roof. As one of the most important features of keeping your home safe, this is unacceptable. Keystone Roofing was created to break this trend.</p>
  <div class="abs about-rule"></div>
  <p class="abs about-body">Our process starts by coming to meet you at your home, learning your needs, and suggesting what we would do if it were our home. We will educate you on suggested materials, installation process, warranty information and available financing.</p>
  <a class="abs read-more">Read more</a>
</section>

<section>
  <h2 class="abs section-title" style="top:1869px">Types of Roofs</h2>
  <div class="abs tabs"><div class="active" style="width:143px">Cedar</div><div style="width:143px">Metal</div><div style="width:112px">Slate</div><div style="width:160px">Asphalt</div><div style="width:128px">Rubber</div></div>
  <div class="abs tile" style="left:235px;top:2050px;background:linear-gradient(135deg,#a2532f,#c7784c 40%,#8a4226 70%,#b86a40)" role="img" aria-label="Photo of cedar shake roofing"></div>
  <div class="abs tile" style="left:484px;top:2050px;background:linear-gradient(135deg,#5e5f60,#8a8b8c 50%,#6b6c6d)" role="img" aria-label="Photo of grey slate roof tiles"></div>
  <div class="abs tile" style="left:734px;top:2050px;background:linear-gradient(135deg,#8a6c5e,#a98f7e 50%,#7c6558)" role="img" aria-label="Photo of weathered asphalt shingle roof"></div>
</section>

<section>
  <div class="abs projects-band"></div>
  <h2 class="abs section-title" style="top:2266px">Recent Projects</h2>
  <div class="abs project project-label" style="left:235px;top:2410px" role="img" aria-label="Darkened photo of a house roof in Lexington">Lexington</div>
  <div class="abs project" style="left:484px;top:2410px;background:linear-gradient(180deg,#dfe8ef 0%,#5a5d62 45%,#e9e9ea 75%,#7a8a5a 100%)" role="img" aria-label="Photo of white colonial house with dormers"></div>
  <div class="abs project" style="left:734px;top:2410px;background:linear-gradient(180deg,#c9d6e2 0%,#555 35%,#7d8a80 70%,#8e9a7c 100%)" role="img" aria-label="Photo of green sided house with new roof"></div>
  <div class="abs project" style="left:235px;top:2595px;background:linear-gradient(180deg,#4d8fd0 0%,#a9c8e6 40%,#3d4248 65%,#e6e6e6 100%)" role="img" aria-label="Photo of shingle-style house under blue sky"></div>
  <div class="abs project" style="left:484px;top:2595px;background:linear-gradient(180deg,#7f9c6a 0%,#3f4a3a 40%,#2f3a33 70%,#5d7a48 100%)" role="img" aria-label="Photo of dark green house among trees"></div>
  <div class="abs project" style="left:734px;top:2595px;background:linear-gradient(180deg,#e8e6e3 0%,#b5a597 40%,#d9d5d0 70%,#c7b8a8 100%)" role="img" aria-label="Photo of cedar shingle house with chimney"></div>
  <div class="abs dots"><i></i><i class="on"></i><i></i></div>
</section>

<section>
  <h2 class="abs section-title" style="top:2913px">Instant Estimate</h2>
  <div class="abs step" style="left:235px;top:3043px"><b>1</b>Choose Your Roof Type</div>
  <div class="abs step" style="left:422px;top:3043px"><b>2</b>About your roof</div>
  <div class="abs step" style="left:609px;top:3043px"><b>3</b>Roof condition</div>
  <div class="abs step" style="left:796px;top:3043px"><b>4</b>Get your cost</div>
  <div class="abs est-card" style="left:235px;top:3099px"><div class="est-swatch" style="background:linear-gradient(180deg,#4a4e4f,#6b7070 50%,#3f4343)" role="img" aria-label="Shingle sample, charcoal"></div><div class="grade">Good</div><div class="model">Ridgeline HDX</div><div class="price">$$$</div><div class="info">View Info</div><div class="btn">Calculate your cost</div></div>
  <div class="abs est-card" style="left:422px;top:3099px"><div class="est-swatch" style="background:linear-gradient(180deg,#7a6054,#9a7c6c 50%,#6d564b)" role="img" aria-label="Shingle sample, brown"></div><div class="grade">Good</div><div class="model">Ridgeline HDX</div><div class="price">$$$</div><div class="info">View Info</div><div class="btn">Calculate your cost</div></div>
  <div class="abs est-card" style="left:609px;top:3099px"><div class="est-swatch" style="background:linear-gradient(180deg,#3f4a58,#5e6c7c 50%,#36404c)" role="img" aria-label="Shingle sample, slate blue"></div><div class="grade">Good</div><div class="model">Ridgeline HDX</div><div class="price">$$$</div><div class="info">View Info</div><div class="btn">Calculate your cost</div></div>
  <div class="abs est-card" style="left:796px;top:3099px"><div class="est-swatch" style="background:linear-gradient(180deg,#4a4848,#656262 50%,#3e3c3c)" role="img" aria-label="Shingle sample, weathered grey"></div><div class="grade">Good</div><div class="model">Ridgeline HDX</div><div class="price">$$$</div><div class="info">View Info</div><div class="btn">Calculate your cost</div></div>
</section>

<section>
  <h2 class="abs section-title" style="top:3496px">Happy Clients</h2>
  <div class="abs chev" style="left:234px">&#8249;</div>
  <div class="abs chev" style="left:941px">&#8250;</div>
  <blockquote class="abs quote">"We needed to put a new roof on our house, as well as repair a sagging porch roof. Shingles had been flying off and we had had several leaks. Dean provided a very rea-sonable estimate - well below some of the other Porchlight List companies. The work was done very promptly and professionally. A couple of issues that arose were set-tled to our satisfaction and Dean took full ownership of the situation. It was very clear that customer satisfaction is a priority for this company. I would definitely recom-mend and hire again."</blockquote>
  <div class="abs quote-tail"></div>
  <div class="abs client"><b>Owen</b><span>Brookfield</span></div>
</section>

<footer>
  <div class="abs footer"></div>
  <div class="abs brand f-brand"><span class="brand-mark"></span><div class="brand-name">KEYSTONE ROOFING</div></div>
  <div class="abs f-addr">48 Alder Ln.<br>Brookfield MA 01506</div>
  <div class="abs f-head" style="left:547px">QUICK LINKS</div>
  <div class="abs f-links" style="left:547px;top:4087px">Home<br>Keystone Roofing<br>Blog<br>Reviews</div>
  <div class="abs f-links" style="left:629px;top:4087px">About<br>Services<br>Affiliations<br>Contact</div>
  <div class="abs f-head" style="left:796px">CONTACT</div>
  <div class="abs f-contact">
    <div><svg width="10" height="10" viewBox="0 0 10 10" fill="none" stroke="#888"><path d="M2 1l2 2-1 1.5a6 6 0 002.5 2.5L7 6l2 2-1.5 1.5C5 9 1 5 .5 2.5z"/></svg>555-014-2290</div>
    <div><svg width="10" height="10" viewBox="0 0 10 10" fill="none" stroke="#888"><path d="M2 1l2 2-1 1.5a6 6 0 002.5 2.5L7 6l2 2-1.5 1.5C5 9 1 5 .5 2.5z"/></svg>555-014-2291</div>
    <div><svg width="10" height="10" viewBox="0 0 10 10" fill="none" stroke="#888"><path d="M1 2h8v6H1zM1 2l4 3 4-3"/></svg>hello@keystoneroofingco.com</div>
  </div>
  <div class="abs f-social"><i></i><i></i><i></i><i></i></div>
</footer>

</body>
</html>
```